Hip / Cool Business Card for Custom Accessory Company

I would like to get a 2 sided design for standard size business cards, glossy (2 inches x 3.5 inches). Can be landscape or portrait layout! The design should include our logo (attached). The card should be extremely clear that the company is Tin Lantern. Should also have our URL clear. Should also use the color scheme seen on our upcoming site, tinlantern-example.com. The font we use is called "hurry up." Other than that, please go-to-town. We are targeting 15-45 y.o. market, with a skew on the 20-30 crowd. We do custom and stock iPhone cases as well as Cufflinks, Winestoppers; see the website for more.
Updates

Project Deadline Extended
Reason: Extending in case the US July 4th Holiday is keeping people from working!!

Industry/Entity Type

Landscape

Requirements
Must have
• Must be clear that the website is tinlantern-example.com. Must be clear that custom designs are an option.
Nice to have
• images of our designs. examples of our designs.
Should not have
• hard on the eyes contrasting colors such as orange on black. green on blue. Should not have any fonts that are considered "old" like Times New Roman. But decorative fonts are fine.

```html
<!DOCTYPE html>
<html lang="en">
<head>
<meta charset="utf-8">
<title>Tin Lantern — Business Card</title>
<link href="https://fonts.googleapis.com/css2?family=Michroma&family=Cinzel:wght@400;500&display=swap" rel="stylesheet">
<style>
  :root {
    --backdrop: #e9e6e1;
    --card: #ffffff;
    --ink: #2b2b2b;
    --teal: #1f9ba6;
    --navy: #0d2f63;
    --navy-deep: #08214a;
    --red: #b3262a;
    --divider: #7fb6d3;
    --muted: #555555;
    --shadow: rgba(0,0,0,0.18);
  }
  * { box-sizing: border-box; margin: 0; padding: 0; }
  html, body { width: 1200px; height: 729px; overflow: hidden; }
  body {
    background: var(--backdrop);
    position: relative;
    font-family: "Cinzel", serif;
  }
  .card {
    position: absolute;
    width: 540px;
    height: 309px;
    background: var(--card);
    box-shadow: 0 6px 18px var(--shadow);
    overflow: hidden;
  }
  .card--front { left: 40px; top: 210px; }
  .card--back  { left: 620px; top: 210px; }

  /* Front */
  .brand {
    position: absolute;
    left: 38px; top: 42px;
    display: flex; align-items: center; gap: 22px;
  }
  .brand__mark {
    width: 92px; height: 92px; border-radius: 50%;
    background: var(--teal);
  }
  .brand__name {
    font-family: "Michroma", sans-serif;
    font-size: 31px;
    color: var(--ink);
    letter-spacing: 1px;
    text-transform: uppercase;
    white-space: nowrap;
  }
  .rule { position: absolute; left: 0; right: 0; height: 2px; background: var(--red); }
  .rule--top { top: 147px; }
  .rule--bottom { top: 188px; }
  .band {
    position: absolute; left: 0; right: 0; top: 153px; height: 30px;
    background: linear-gradient(90deg, var(--navy-deep), var(--navy) 60%, var(--teal));
    display: flex; align-items: center; padding-left: 150px; gap: 14px;
    color: #fff;
    white-space: nowrap;
  }
  .band__name { font-size: 16px; letter-spacing: 1px; }
  .band__role { font-size: 12px; letter-spacing: 1px; text-transform: uppercase; }
  .address {
    position: absolute; left: 14px; top: 212px; width: 222px;
    text-align: right; color: var(--red);
    font-size: 11px; line-height: 1.5; text-transform: uppercase; letter-spacing: 0.3px;
    white-space: nowrap;
  }
  .divider { position: absolute; left: 248px; top: 200px; width: 1px; height: 72px; background: var(--divider); }
  .contacts {
    position: absolute; left: 262px; top: 203px; list-style: none;
    font-size: 11px; color: var(--muted); line-height: 1; letter-spacing: 0.4px;
    white-space: nowrap;
  }
  .contacts li { display: flex; align-items: center; gap: 7px; height: 16px; }
  .contacts svg { width: 10px; height: 10px; flex: none; }
  .contacts .upper { text-transform: uppercase; }

  /* Back */
  .emblem {
    position: absolute; inset: 0;
    display: flex; flex-direction: column; align-items: center; justify-content: center; gap: 10px;
  }
  .emblem__word {
    font-family: "Michroma", sans-serif;
    font-size: 34px; color: #111; letter-spacing: 2px; text-transform: uppercase;
  }
  .emblem__mark { width: 130px; height: 130px; border-radius: 50%; background: var(--teal); }
</style>
</head>
<body>

<section class="card card--front" aria-label="Card front">
  <div class="brand">
    <div class="brand__mark"></div>
    <div class="brand__name">Tin Lantern</div>
  </div>
  <div class="rule rule--top"></div>
  <div class="band">
    <span class="band__name">Dana Whitlow</span>
    <span class="band__role">Custom Design Consultant</span>
  </div>
  <div class="rule rule--bottom"></div>

  <p class="address">48 Orchard Lane, Bay Road,<br>Australia</p>
  <div class="divider"></div>
  <ul class="contacts">
    <li>
      <svg viewBox="0 0 10 10"><circle cx="5" cy="5" r="5" fill="var(--red)"/><path d="M3.2 2.6c.4-.3.8 0 1 .5l.2.5-.5.5c.3.7.8 1.2 1.5 1.5l.5-.5.5.2c.5.2.8.6.5 1-.5.6-1.3.6-2.2 0C3.8 6 3 5 2.8 4.1c-.1-.6 0-1.2.4-1.5z" fill="#fff"/></svg>
      07700 900412
    </li>
    <li>
      <svg viewBox="0 0 10 10"><circle cx="5" cy="5" r="5" fill="var(--red)"/><rect x="3.3" y="2.2" width="3.4" height="5.6" rx=".6" fill="#fff"/></svg>
      0117 496 0733
    </li>
    <li class="upper">
      <svg viewBox="0 0 10 10"><circle cx="5" cy="5" r="5" fill="var(--red)"/><rect x="2.3" y="3" width="5.4" height="4" fill="#fff"/><path d="M2.3 3L5 5.2 7.7 3" stroke="var(--red)" stroke-width=".7" fill="none"/></svg>
      hello@tinlantern-example.com
    </li>
    <li class="upper">
      <svg viewBox="0 0 10 10"><circle cx="5" cy="5" r="5" fill="var(--red)"/><circle cx="5" cy="5" r="2.8" stroke="#fff" stroke-width=".7" fill="none"/><path d="M2.2 5h5.6M5 2.2c-1.4 1.6-1.4 4 0 5.6M5 2.2c1.4 1.6 1.4 4 0 5.6" stroke="#fff" stroke-width=".6" fill="none"/></svg>
      www.tinlantern-example.com
    </li>
  </ul>
</section>

<section class="card card--back" aria-label="Card back">
  <div class="emblem">
    <div class="emblem__word">Tin</div>
    <div class="emblem__mark"></div>
    <div class="emblem__word">Lantern</div>
  </div>
</section>

</body>
</html>
```